Lumo -Fresh business card design

It is a dry cleaning carpet business.
Red wine stain removal and pet urine treatments.
Servicing all regional areas.

all logo and pictures files have been uploaded

Industry/Entity Type

Dry Cleaning

Contact Information for Business Card

Lumo-Fresh Carpet and upholstery cleaning.
Servicing Albury/Wodonga and surrounding areas.
ph greg 0413572960 ,email lumofresh1@kestrelmail.com

Font styles to use
Serif
Sans Serif
Other font styles liked:
• lumo fresh logo font

Colors
ec2027
ffcf3e
33a6d7
0692cd

Requirements
Nice to have
• I have included photos of the logo and car and stripe on van ,I dont need all of them in the card just i would like to stick to these colours.

```html
<!DOCTYPE html>
<html lang="en">
<head>
<meta charset="utf-8">
<title>Lumo-Fresh Business Card</title>
<link rel="stylesheet" href="https://fonts.googleapis.com/css2?family=Montserrat:wght@800&family=Didact+Gothic&family=Open+Sans:wght@600&display=swap">
<style>
  :root {
    --bg: #e9ecef;
    --card-white: #ffffff;
    --card-shade: #eef0f2;
    --brand-blue: #0692cd;
    --sky-blue: #33a6d7;
    --deep-blue: #1f6fc4;
    --tagline-blue: #4f86d4;
    --accent-red: #ec2027;
    --ink: #2b2b2b;
    --on-blue: #ffffff;
  }
  * { margin: 0; padding: 0; box-sizing: border-box; }
  html, body {
    width: 1200px; height: 901px; overflow: hidden;
    background: var(--bg);
  }
  .stage {
    position: relative; width: 1200px; height: 901px;
    display: flex; align-items: center; justify-content: center;
  }
  .card {
    position: relative; width: 1000px; height: 571px;
    border-radius: 64px; overflow: hidden;
    background: linear-gradient(160deg, var(--card-white) 0%, var(--card-shade) 100%);
    box-shadow: 0 18px 40px rgba(0,0,0,0.18);
  }
  .card__swoosh { position: absolute; inset: 0; width: 100%; height: 100%; }
  .brand {
    position: absolute; left: 62px; top: 62px; width: 440px; text-align: center;
  }
  .brand__name {
    font-family: "Montserrat", sans-serif; font-weight: 800;
    font-size: 66px; letter-spacing: 2px; color: var(--brand-blue);
    line-height: 1;
  }
  .brand__tagline {
    margin-top: 10px;
    font-family: "Open Sans", sans-serif; font-weight: 600;
    font-size: 25px; line-height: 1.1; color: var(--tagline-blue);
  }
  .person {
    position: absolute; right: 70px; top: 132px; text-align: left; width: 330px;
  }
  .person__name {
    font-family: "Didact Gothic", sans-serif; font-size: 34px;
    letter-spacing: 1.5px; color: var(--accent-red);
  }
  .person__role {
    font-family: "Didact Gothic", sans-serif; font-size: 25px;
    color: var(--ink); margin-top: 4px; padding-left: 36px;
  }
  .contact {
    position: absolute; right: 54px; top: 352px; text-align: right;
    font-family: "Didact Gothic", sans-serif; color: var(--on-blue);
  }
  .contact__address { font-size: 21px; line-height: 1.3; margin-bottom: 16px; }
  .contact__line {
    display: flex; justify-content: flex-end; align-items: center; gap: 10px;
    font-size: 20px; line-height: 1; margin-bottom: 12px;
  }
  .contact__icon { width: 18px; height: 18px; flex: none; }
</style>
</head>
<body>
<main class="stage">
  <section class="card" aria-label="Lumo-Fresh business card">
    <svg class="card__swoosh" viewBox="0 0 1000 571" preserveAspectRatio="none" aria-hidden="true">
      <defs>
        <linearGradient id="swooshFill" x1="0" y1="1" x2="1" y2="0">
          <stop offset="0" stop-color="#1b5fb8"/>
          <stop offset="0.55" stop-color="#0692cd"/>
          <stop offset="1" stop-color="#1f7fd6"/>
        </linearGradient>
      </defs>
      <path d="M40,468 C380,470 720,380 1000,120 L1000,571 L0,571 L0,468 Z" fill="#33a6d7"/>
      <path d="M40,478 C390,478 740,392 1000,150" fill="none" stroke="#ffffff" stroke-width="4"/>
      <path d="M20,492 C400,492 750,402 1000,170 L1000,571 L0,571 L0,492 Z" fill="url(#swooshFill)"/>
    </svg>

    <div class="brand">
      <div class="brand__name">LUMO-FRESH</div>
      <div class="brand__tagline">CARPET &amp; UPHOLSTERY<br>CLEANING</div>
    </div>

    <div class="person">
      <div class="person__name">DANIEL FOSTER</div>
      <div class="person__role">Managing Director</div>
    </div>

    <address class="contact" style="font-style:normal">
      <div class="contact__address">071 12th floor,Park<br>Harbour Road KLM</div>
      <div class="contact__line">012 468 1357
        <svg class="contact__icon" viewBox="0 0 24 24" aria-hidden="true"><path fill="#fff" d="M6.6 10.8a15 15 0 0 0 6.6 6.6l2.2-2.2c.3-.3.7-.4 1-.2 1.1.4 2.3.6 3.6.6.6 0 1 .4 1 1V20c0 .6-.4 1-1 1A17 17 0 0 1 3 4c0-.6.4-1 1-1h3.5c.6 0 1 .4 1 1 0 1.3.2 2.5.6 3.6.1.3 0 .7-.2 1z"/></svg>
      </div>
      <div class="contact__line">012 468 1357
        <svg class="contact__icon" viewBox="0 0 24 24" aria-hidden="true"><rect x="6" y="2" width="12" height="20" rx="2" fill="none" stroke="#fff" stroke-width="2"/><circle cx="12" cy="18" r="1.2" fill="#fff"/></svg>
      </div>
      <div class="contact__line">012 468 1357
        <svg class="contact__icon" viewBox="0 0 24 24" aria-hidden="true"><rect x="4" y="9" width="16" height="12" rx="1" fill="#fff"/><rect x="7" y="3" width="10" height="7" fill="none" stroke="#fff" stroke-width="2"/></svg>
      </div>
      <div class="contact__line">yourname@mailbox.com
        <svg class="contact__icon" viewBox="0 0 24 24" aria-hidden="true"><rect x="2" y="5" width="20" height="14" rx="1" fill="#fff"/><path d="M2 6l10 7 10-7" fill="none" stroke="#1f6fc4" stroke-width="1.6"/></svg>
      </div>
      <div class="contact__line">www.yourwebsite.com
        <svg class="contact__icon" viewBox="0 0 24 24" aria-hidden="true"><circle cx="12" cy="12" r="9" fill="none" stroke="#fff" stroke-width="2"/><ellipse cx="12" cy="12" rx="4" ry="9" fill="none" stroke="#fff" stroke-width="1.6"/><path d="M3 12h18" stroke="#fff" stroke-width="1.6"/></svg>
      </div>
    </address>
  </section>
</main>
</body>
</html>
```